Business Card Design

We need a business card design for a new company. We produce and sell fully grown topiary (please Google topiary pictures if you are not familiar with Topiary).We make many different topiary designs and shapes in all sizes. Ranging from cute little table top animal sculptures such as bunnies and swans for the indoors, to big sculptures such as actual size elephants for outdoor gardens and parks. We also make topiary balls, spiral shapes and other attractive geometrical shapes for indoor and outdoor decorations. We want to see designs that reflects the playfulness and ,liveliness and cute characteristics of our products.Please find attached the logo.Thank you

Industry/Entity Type

Business

Contact Information for Business Card

Company Name : Leaf Forge
Slogan : Shaping Every Garden Bright
Tagline: Topiary...and more
Website : www.leafforge.example

Name on Card : Youssef Nabil Darwish
Title : Founder & CEO
email: youssef_nabil@leafforge.example

Address : 27 El-Masry Street
Ground Floor,Ste.1
El-Marg,Cairo,Egypt

Office Telephone : (02) 25948017
Mobile Number : 01287719462

Requirements
Must have
• The business card must have a white background.

```html
<!DOCTYPE html>
<html lang="en">
<head>
<meta charset="utf-8">
<title>Leaf Forge — Business Card</title>
<link rel="stylesheet" href="https://fonts.googleapis.com/css2?family=Architects+Daughter&family=Montserrat:wght@700&family=Questrial&display=swap">
<style>
  :root {
    --page: #e9ebe6;
    --card-white: #ffffff;
    --leaf: #4f9a3a;
    --leaf-deep: #3d7f2c;
    --leaf-light: #6fb44f;
    --topiary-dark: #3f7a28;
    --topiary-light: #7fb85a;
    --ink-soft: #666666;
  }
  * { margin: 0; padding: 0; box-sizing: border-box; }
  html, body { width: 1200px; height: 800px; overflow: hidden; }
  body {
    background: var(--page);
    position: relative;
    font-family: "Questrial", Arial, sans-serif;
  }
  .card {
    position: absolute;
    left: 100px; top: 110px;
    width: 1000px; height: 580px;
    background: var(--card-white);
    overflow: hidden;
    box-shadow: 0 6px 24px rgba(0,0,0,0.15);
  }
  .card-band { position: absolute; inset: 0; width: 100%; height: 100%; }
  .brand {
    position: absolute; left: 60px; top: 58px;
  }
  .brand-name {
    font-family: "Architects Daughter", cursive;
    font-size: 96px; line-height: 1;
    color: var(--leaf);
    letter-spacing: 1px;
    white-space: nowrap;
  }
  .brand-slogan {
    font-family: "Architects Daughter", cursive;
    font-size: 30px;
    color: var(--leaf);
    margin-top: 6px;
    margin-left: 14px;
    white-space: nowrap;
  }
  .brand-tagline {
    position: absolute; left: 400px; top: 236px;
    font-family: "Architects Daughter", cursive;
    font-size: 26px;
    color: var(--leaf-deep);
    white-space: nowrap;
  }
  .holder {
    position: absolute; right: 40px; top: 30px;
    text-align: right;
  }
  .holder-name {
    font-family: "Montserrat", Arial, sans-serif;
    font-weight: 700; font-size: 20px;
    color: var(--leaf);
  }
  .holder-title {
    font-size: 14px; color: var(--ink-soft); margin-top: 2px;
  }
  .topiary-art {
    position: absolute; right: 24px; top: 150px;
    width: 296px; height: 300px;
    border-radius: 46% 52% 30% 30% / 48% 50% 20% 20%;
    background: radial-gradient(ellipse at 45% 40%, var(--topiary-light), var(--topiary-dark) 75%);
  }
  .contact {
    position: absolute; left: 56px; top: 340px;
    list-style: none;
    color: var(--card-white);
    font-size: 27px; line-height: 38px;
  }
  .contact-item { display: flex; align-items: flex-start; gap: 12px; white-space: nowrap; }
  .contact-icon { width: 26px; height: 26px; margin-top: 6px; flex: none; }
  .contact-icon--blank { visibility: hidden; }
</style>
</head>
<body>
  <article class="card">
    <svg class="card-band" viewBox="0 0 1000 580" preserveAspectRatio="none" aria-hidden="true">
      <defs>
        <linearGradient id="band-fill" x1="0" y1="0" x2="0" y2="1">
          <stop offset="0" stop-color="var(--leaf-light)"/>
          <stop offset="1" stop-color="var(--leaf-deep)"/>
        </linearGradient>
      </defs>
      <path d="M0 300 C 220 250, 520 250, 1000 300 L1000 580 L0 580 Z" fill="url(#band-fill)"/>
      <path d="M0 318 C 240 300, 460 300, 720 292 C 460 318, 240 330, 0 352 Z" fill="var(--card-white)"/>
      <circle cx="960" cy="150" r="110" fill="none" stroke="#eeeeee" stroke-width="3"/>
    </svg>

    <header class="brand">
      <h1 class="brand-name">Leaf Forge</h1>
      <p class="brand-slogan">Shaping Every Garden Bright</p>
    </header>
    <p class="brand-tagline">Topiary...and more</p>

    <div class="holder">
      <p class="holder-name">Youssef Nabil Darwish</p>
      <p class="holder-title">Founder &amp; CEO</p>
    </div>

    <div class="topiary-art" role="img" aria-label="Photograph of green topiary sculptures: an elephant, a spiral tree and a small bunny"></div>

    <ul class="contact">
      <li class="contact-item">
        <svg class="contact-icon" viewBox="0 0 24 24" aria-hidden="true"><path fill="#fff" d="M6.6 10.8a15 15 0 0 0 6.6 6.6l2.2-2.2c.3-.3.7-.4 1-.2 1.1.4 2.3.6 3.6.6.6 0 1 .4 1 1V20c0 .6-.4 1-1 1A17 17 0 0 1 3 4c0-.6.4-1 1-1h3.5c.6 0 1 .4 1 1 0 1.3.2 2.5.6 3.6.1.3 0 .7-.2 1z"/></svg>
        <span>(02) 25948017</span>
      </li>
      <li class="contact-item">
        <svg class="contact-icon" viewBox="0 0 24 24" aria-hidden="true"><rect x="6" y="2" width="12" height="20" rx="2" fill="none" stroke="#fff" stroke-width="2"/><rect x="8.5" y="5" width="7" height="9" fill="#fff"/><circle cx="12" cy="18" r="1.3" fill="#fff"/></svg>
        <span>01287719462</span>
      </li>
      <li class="contact-item">
        <svg class="contact-icon" viewBox="0 0 24 24" aria-hidden="true"><g fill="none" stroke="#fff" stroke-width="1.8"><circle cx="12" cy="12" r="9.5"/><ellipse cx="12" cy="12" rx="4" ry="9.5"/><path d="M2.5 12h19M4 7h16M4 17h16"/></g></svg>
        <span>www.leafforge.example</span>
      </li>
      <li class="contact-item">
        <svg class="contact-icon" viewBox="0 0 24 24" aria-hidden="true"><rect x="2" y="5" width="20" height="14" rx="2" fill="#fff"/><path d="M3 6l9 7 9-7" fill="none" stroke="var(--leaf)" stroke-width="1.8"/></svg>
        <span>youssef_nabil@leafforge.example</span>
      </li>
      <li class="contact-item">
        <svg class="contact-icon" viewBox="0 0 24 24" aria-hidden="true"><path fill="#fff" d="M12 3 2 12h3v9h5v-6h4v6h5v-9h3z"/></svg>
        <span>27 El-Masry Street Ground Floor,</span>
      </li>
      <li class="contact-item">
        <svg class="contact-icon contact-icon--blank" viewBox="0 0 24 24" aria-hidden="true"></svg>
        <span>Ste.1 El-Marg,Cairo,Egypt</span>
      </li>
    </ul>
  </article>
</body>
</html>
```